QV Holdings Website Redesign Contest

We want to refresh our website to be more insitutional, professional for an international audience. We have designed a new logo for this purpose and that has been attached. A full brand brief and positioning statement has also been attached. Please read through all the documents carefully before designing. The old website is found here: https://qv-holdings.example/

Target Market(s)

Actuaries and associated businesses internationally

Industry/Entity Type

professional services - actuaries

Number of Pages Required

3 page

Font styles to use
Sans Serif

Colors
0054AA
0677BA
7BADD7
CADEEF
E8F1F8
0094D4
00A9DD
6FCCEA
C7EBF8
E9F6FB
F0912C
F2A743
F7CA91
FBE8D2
FDF5EE
EE7325
F08F49
F5BC92
FAE3D3
FDF4ED
EB3D1F
EC4F4E
F09395
F8D3D4
FCEDEE

Requirements
Must have
• blues and greens to match the logo color, complimentary colors, navigation
Nice to have
• old site: https://qv-holdings.example/

```html
<!DOCTYPE html>
<html lang="en">
<head>
<meta charset="utf-8">
<title>QV Holdings — Actuarial Software</title>
<link href="https://fonts.googleapis.com/css2?family=Inter:wght@400;500;600;700&display=swap" rel="stylesheet">
<style>
:root{
  --stage:#b3b3b3;
  --brand-blue:#0a52f5;
  --navy:#04224a;
  --navy-deep:#021a3a;
  --orange:#ff7300;
  --ice:#e6f0f7;
  --card:#f7f9fc;
  --card-line:#dfe6ee;
  --text:#3a3f47;
  --muted:#555b63;
  --white:#ffffff;
  --black:#000000;
}
*{margin:0;padding:0;box-sizing:border-box}
html,body{width:1200px;height:2180px;overflow:hidden}
body{background:var(--stage);font-family:'Inter',sans-serif;color:var(--text);position:relative}
.page{position:absolute;left:106px;top:106px;width:988px;background:var(--white);box-shadow:0 10px 40px rgba(0,0,0,.25)}

.site-header{height:56px;background:var(--brand-blue);position:relative}
.brand-area{position:absolute;left:0;top:0;height:56px;width:300px;background:var(--white)}
.brand-name{position:absolute;left:16px;top:15px;font-size:22px;font-weight:600;color:var(--navy);letter-spacing:.5px;display:flex;align-items:center;gap:8px}
.brand-name .mark{width:12px;height:12px;background:var(--brand-blue)}
.main-nav{position:absolute;left:329px;top:0;height:56px;display:flex;align-items:center;gap:20px}
.main-nav a{color:var(--white);font-size:13px;text-decoration:none}
.btn{display:inline-block;background:var(--orange);color:var(--white);font-weight:600;text-decoration:none;border-radius:2px}
.site-header .btn{position:absolute;right:11px;top:12px;font-size:13px;padding:8px 13px}

.hero{height:321px;position:relative;text-align:center;color:var(--white)}
.hero-bg{position:absolute;inset:0;background:linear-gradient(160deg,#062850 0%,var(--navy) 45%,var(--navy-deep) 100%)}
.hero-content{position:relative;padding-top:68px}
.hero h1{font-size:28px;font-weight:700;line-height:37px;width:600px;margin:0 auto}
.hero p{font-size:13px;line-height:22px;width:620px;margin:14px auto 0}
.hero .btn{font-size:11.5px;padding:11px 23px;margin-top:21px}

.section-title{color:var(--brand-blue);font-size:23px;font-weight:700;text-align:center}
.overview{height:230px;background:var(--ice);padding-top:50px}
.overview p{width:555px;margin:24px auto 0;font-size:12px;line-height:20.3px;text-align:center;color:var(--muted)}

.core{height:369px;padding-top:50px}
.solution-grid{width:777px;margin:24px auto 0;display:flex;gap:17px}
.solution-card{width:248px;height:220px;background:var(--card);border:1px solid var(--card-line);border-radius:3px;text-align:center;padding:26px 10px 0}
.solution-card svg{display:block;margin:0 auto}
.solution-card h3{color:var(--brand-blue);font-size:14px;font-weight:700;margin-top:16px;white-space:nowrap;letter-spacing:-.1px}
.solution-card p{font-size:11.5px;line-height:17px;margin:11px 8px 0;color:var(--muted)}
.more{color:var(--orange);font-size:11px;font-weight:600;text-decoration:none;display:inline-block;margin-top:9px}

.characteristics{height:276px;background:var(--ice);padding-top:50px}
.trait-grid{width:706px;margin:24px auto 0;display:grid;grid-template-columns:362px 344px;row-gap:22px}
.trait{position:relative;padding-left:20px}
.trait::before{content:"";position:absolute;left:0;top:3px;width:8px;height:8px;border-radius:50%;background:var(--orange)}
.trait h4{color:var(--brand-blue);font-size:12.5px;font-weight:700}
.trait p{font-size:10.5px;line-height:16px;margin-top:5px;color:var(--muted);width:322px}

.insights{height:327px;padding-top:50px}
.insight-grid{width:706px;margin:24px auto 0;display:flex;gap:17px}
.insight-card{width:224px;height:177px;background:#f9f9f9;border-left:3px solid var(--brand-blue);padding:18px 14px 0 17px}
.insight-card h3{color:var(--brand-blue);font-size:12.5px;font-weight:700;line-height:21px;letter-spacing:-.15px}
.insight-card p{font-size:10.5px;line-height:16px;margin-top:6px;color:var(--muted)}
.insight-card .more{font-size:10.5px;margin-top:9px}

.cta{height:178px;background:var(--brand-blue);text-align:center;padding-top:48px}
.cta h2{color:var(--white);font-size:22px;font-weight:600}
.cta .btn{font-size:11.5px;padding:11px 23px;margin-top:22px}

.site-footer{height:212px;background:var(--black);color:var(--white);padding-top:38px}
.footer-cols{width:777px;margin:0 auto;display:flex}
.footer-col{width:200px}
.footer-col h5{font-size:11.5px;font-weight:600;margin-bottom:12px}
.footer-col a{display:block;color:var(--white);font-size:10px;text-decoration:none;margin-bottom:8px}
.copyright{text-align:center;font-size:8.5px;color:#cfcfcf;margin-top:22px}
</style>
</head>
<body>
<div class="page">
  <header class="site-header">
    <div class="brand-area">
      <div class="brand-name"><span class="mark"></span>QV Holdings</div>
    </div>
    <nav class="main-nav">
      <a href="#">Home</a><a href="#">Platform</a><a href="#">Solutions</a><a href="#">Insights</a><a href="#">Company</a><a href="#">Contact</a>
    </nav>
    <a class="btn" href="#">Request a Technical Walkthrough</a>
  </header>

  <section class="hero">
    <div class="hero-bg" role="img" aria-label="Dark navy background with faint network lines and nodes"></div>
    <div class="hero-content">
      <h1>Actuarial software for structured, auditable financial analysis</h1>
      <p>Software that translates actuarial methodologies into disciplined decision-ready analytical tools across diverse regulatory environments.</p>
      <a class="btn" href="#">Request a Technical Walkthrough</a>
    </div>
  </section>

  <section class="overview">
    <h2 class="section-title">Platform Overview</h2>
    <p>QV Holdings develops modular actuarial software designed to support reserving, valuation, pricing and enterprise risk management workflows across diverse regulatory environments. Our platform translates established actuarial methodologies into disciplined, audit-ready tools, ensuring transparency and governance at every step.</p>
  </section>

  <section class="core">
    <h2 class="section-title">Core Solutions</h2>
    <div class="solution-grid">
      <div class="solution-card">
        <svg width="20" height="22" viewBox="0 0 20 22" fill="none" stroke="#555" stroke-width="1"><rect x="2" y="1" width="16" height="20" rx="1"/><path d="M6 8h8M6 11h8M6 14h8"/></svg>
        <h3>Reserving &amp; Valuation</h3>
        <p>Structured workflows and financial reporting across jurisdictions built on disciplined actuarial methodologies.</p>
        <a class="more" href="#">Learn more →</a>
      </div>
      <div class="solution-card">
        <svg width="20" height="22" viewBox="0 0 20 22" fill="none" stroke="#555" stroke-width="1"><rect x="3" y="13" width="3" height="6"/><rect x="8.5" y="9" width="3" height="10"/><rect x="14" y="5" width="3" height="14"/></svg>
        <h3>Pricing</h3>
        <p>Insurance and reinsurance pricing models grounded in transparency, enabling accurate, explainable decisions.</p>
        <a class="more" href="#">Learn more →</a>
      </div>
      <div class="solution-card">
        <svg width="20" height="22" viewBox="0 0 20 22" fill="none" stroke="#555" stroke-width="1"><path d="M10 2L3 5v6c0 4 3 7 7 9 4-2 7-5 7-9V5z"/></svg>
        <h3>Enterprise Risk Management</h3>
        <p>Tools supporting reinsurance optimization and capital modeling for comprehensive enterprise risk management.</p>
        <a class="more" href="#">Learn more →</a>
      </div>
    </div>
  </section>

  <section class="characteristics">
    <h2 class="section-title">Platform Characteristics</h2>
    <div class="trait-grid">
      <div class="trait"><h4>Structured Workflows</h4><p>Disciplined processes built to support multi-jurisdictional review and actuarial governance.</p></div>
      <div class="trait"><h4>Transparent Assumptions</h4><p>Clear documentation of assumptions and methodologies for auditability and defensibility.</p></div>
      <div class="trait"><h4>Comparative Analysis</h4><p>Capabilities for scenario comparison and sensitivity analysis to inform professional judgment.</p></div>
      <div class="trait"><h4>Governance Ready</h4><p>Outputs designed to support regulator and board review, ensuring compliance and clarity.</p></div>
    </div>
  </section>

  <section class="insights">
    <h2 class="section-title">Insights</h2>
    <div class="insight-grid">
      <article class="insight-card">
        <h3>Methodological Perspectives in Actuarial Reserving</h3>
        <p>How disciplined methodologies enhance reserving accuracy and governance across markets.</p>
        <a class="more" href="#">Read more →</a>
      </article>
      <article class="insight-card">
        <h3>Governance Considerations in Multi-Jurisdictional Analysis</h3>
        <p>Best practices for supporting regulated environments with transparent, auditable processes.</p>
        <a class="more" href="#">Read more →</a>
      </article>
      <article class="insight-card">
        <h3>Observations on Actuarial Practice in Emerging Markets</h3>
        <p>Lessons from diverse regulatory contexts and their implications for modern actuarial software.</p>
        <a class="more" href="#">Read more →</a>
      </article>
    </div>
  </section>

  <section class="cta">
    <h2>Interested in exploring the platform?</h2>
    <a class="btn" href="#">Request a Technical Walkthrough</a>
  </section>

  <footer class="site-footer">
    <div class="footer-cols">
      <div class="footer-col"><h5>Company</h5><a href="#">About</a><a href="#">Careers</a><a href="#">Legal</a></div>
      <div class="footer-col"><h5>Platform</h5><a href="#">Overview</a><a href="#">Reserving &amp; Valuation</a><a href="#">Pricing</a><a href="#">Enterprise Risk Management</a></div>
      <div class="footer-col"><h5>Insights</h5><a href="#">Articles</a><a href="#">Guides</a><a href="#">News</a></div>
      <div class="footer-col"><h5>Contact</h5><a href="#">Email Us</a><a href="#">Request a Walkthrough</a></div>
    </div>
    <p class="copyright">© 2026 QV Holdings. All rights reserved.</p>
  </footer>
</div>
</body>
</html>
```